Stationary Design for Norvack Digital

We are after a full stationary back business cards, letterheads, compliment slip, invoice template, delivery note and anything else we could use within the stationary pack.

We would also like an email footer creating.

Our company details to be included on all stationary:

Registered Name: Norvack Limited
Company Registration Number: 20483957
Website: www.norvackdigital.example
email: info@norvackdigital.example
Phone: 01632 960 417
Address: 48 Elmstead Lane Loughborough Leicestershire United Kingdom LE14 7QW

Industry/Entity Type

Business

```html
<!DOCTYPE html>
<html lang="en">
<head>
<meta charset="utf-8">
<title>Norvack Digital – Stationery</title>
<link rel="stylesheet" href="https://fonts.googleapis.com/css2?family=Arimo:wght@400;700&family=Noto+Serif:wght@400;700&display=swap">
<style>
  :root{
    --bg:#a3bde0;
    --navy:#234a7c;
    --paper:#ffffff;
    --ink:#1d1d1d;
    --brand-ink:#2c4f80;
  }
  *{box-sizing:border-box;margin:0;padding:0}
  html,body{width:1200px;height:800px;overflow:hidden;background:var(--bg)}
  .canvas{position:relative;width:1200px;height:800px}
  .sheet{position:absolute;background:var(--paper);overflow:hidden}
  .swoosh{position:absolute;left:0;width:100%}
  .brand{font-family:"Arimo",sans-serif;font-weight:400;letter-spacing:.06em;color:var(--brand-ink);white-space:nowrap;position:absolute}
  .brand--light{color:#fff}
  .details{font-family:"Noto Serif",serif;color:var(--brand-ink);position:absolute;line-height:1.3}
  .details strong{font-weight:700;display:block}

  /* folder */
  .folder{left:82px;top:120px;width:318px;height:448px;background:var(--navy)}
  .folder .brand{left:0;right:0;top:205px;text-align:center;font-size:26px}

  /* letterhead */
  .letterhead{left:432px;top:120px;width:318px;height:448px}
  .letterhead .brand{right:36px;top:42px;font-size:12px}
  .letter{position:absolute;left:44px;top:118px;width:250px;font-family:"Arimo",sans-serif;font-size:6.2px;line-height:1.28;color:var(--ink)}
  .letter p{margin-bottom:7px}
  .letterhead .swoosh{top:0;height:100%}
  .letterhead .details{left:224px;top:393px;font-size:3.6px}
  .letterhead .details span{display:block;margin-top:3px}

  /* envelope front */
  .envelope-front{left:782px;top:209px;width:328px;height:162px}
  .envelope-front .details{left:30px;top:22px;font-size:4.6px}
  .envelope-front .details strong{font-size:7.6px}
  .envelope-front .brand{right:26px;top:38px;font-size:14px}
  .envelope-front .swoosh{top:0;height:100%}

  /* envelope back */
  .envelope-back{left:782px;top:402px;width:330px;height:162px}
  .envelope-back .swoosh{top:0;height:100%}
  .envelope-back .details{left:35px;top:98px;font-size:4.6px}
  .envelope-back .details strong{font-size:7.6px}
  .envelope-back .brand{right:30px;top:122px;font-size:14px}

  /* tube banner */
  .banner{position:absolute;left:195px;top:602px;width:565px;height:90px;background:var(--navy);border-radius:14px}
  .banner .brand{left:0;right:0;top:30px;text-align:center;font-size:26px}

  /* business cards */
  .card-front{left:812px;top:606px;width:136px;height:78px}
  .card-front .name{position:absolute;left:12px;top:16px;font-family:"Noto Serif",serif;font-weight:700;font-size:3.6px;color:var(--ink)}
  .card-front .brand{right:12px;top:14px;font-size:6.5px}
  .card-front .details{left:12px;top:28px;font-size:2.6px}
  .card-front .details strong{font-size:4.4px}
  .card-front .swoosh{top:0;height:100%}
  .card-back{left:975px;top:606px;width:135px;height:78px;background:var(--navy)}
  .card-back .brand{left:0;right:0;top:33px;text-align:center;font-size:10px}
</style>
</head>
<body>
<main class="canvas">

  <section class="sheet folder" aria-label="Presentation folder cover">
    <span class="brand brand--light">NORVACK DIGITAL</span>
  </section>

  <section class="sheet letterhead" aria-label="Letterhead">
    <span class="brand">NORVACK DIGITAL</span>
    <div class="letter">
      <p>To John Doe</p>
      <p style="margin-top:14px">What is Lorem Ipsum?<br>Lorem Ipsum is simply dummy text of the printing and typesetting industry. Lorem Ipsum has been the industry's standard dummy text ever since the 1500s, when an unknown printer took a galley of type and scrambled it to make a type specimen book. It has survived not only five centuries, but also the leap into electronic typesetting, remaining essentially unchanged. It was popularised in the 1960s with the release of Typesheet sheets containing Lorem Ipsum passages, and more recently with desktop publishing software like Quillset Layout including versions of Lorem Ipsum.</p>
      <p>Why do we use it?<br>It is a long established fact that a reader will be distracted by the readable content of a page when looking at its layout. The point of using Lorem Ipsum is that it has a more-or-less normal distribution of letters, as opposed to using 'Content here, content here', making it look like readable English. Many desktop publishing packages and web page editors now use Lorem Ipsum as their default model text, and a search for 'lorem ipsum' will uncover many web sites still in their infancy. Various versions have evolved over the years, sometimes by accident, sometimes on purpose (injected humour and the like).</p>
      <p>Sincerely,<br>John Doe</p>
    </div>
    <svg class="swoosh" viewBox="0 0 100 100" preserveAspectRatio="none" aria-hidden="true">
      <path fill="var(--navy)" d="M0,79.5 C12,88 45,91 100,76 L100,77.2 C55,97 18,97 0,90 Z"/>
    </svg>
    <div class="details">
      <strong>Norvack Limited</strong>
      Company Registration Number: 20483957<br>
      Address: 48 Elmstead Lane Loughborough<br>
      Leicestershire United Kingdom LE14 7QW
      <span>www.norvackdigital.example<br>info@norvackdigital.example<br>Phone: 01632 960 417</span>
    </div>
  </section>

  <section class="sheet envelope-front" aria-label="Envelope front">
    <div class="details">
      <strong>Norvack Limited</strong>
      Company Registration Number: 20483957<br>
      Website: www.norvackdigital.example<br>
      email: info@norvackdigital.example<br>
      Phone: 01632 960 417<br>
      Address: 48 Elmstead Lane Loughborough<br>
      Leicestershire United Kingdom LE14 7QW
    </div>
    <span class="brand">NORVACK DIGITAL</span>
    <svg class="swoosh" viewBox="0 0 100 100" preserveAspectRatio="none" aria-hidden="true">
      <path fill="var(--navy)" d="M0,60 C8,80 50,85 100,50 L100,53 C55,100 12,100 0,85 Z"/>
    </svg>
  </section>

  <section class="sheet envelope-back" aria-label="Envelope back">
    <svg class="swoosh" viewBox="0 0 100 100" preserveAspectRatio="none" aria-hidden="true">
      <path fill="var(--navy)" d="M0,0 H100 V4 C85,30 50,40 38,42 C22,44 8,34 0,24 Z"/>
    </svg>
    <div class="details">
      <strong>Norvack Limited</strong>
      Company Registration Number: 20483957<br>
      Website: www.norvackdigital.example<br>
      email: info@norvackdigital.example<br>
      Phone: 01632 960 417<br>
      Address: 48 Elmstead Lane Loughborough<br>
      Leicestershire United Kingdom LE14 7QW
    </div>
    <span class="brand">NORVACK DIGITAL</span>
  </section>

  <section class="banner" aria-label="Poster tube wrap">
    <span class="brand brand--light">NORVACK DIGITAL</span>
  </section>

  <section class="sheet card-front" aria-label="Business card front">
    <span class="name">JOHN DOE</span>
    <span class="brand">NORVACK DIGITAL</span>
    <div class="details">
      <strong>Norvack Limited</strong>
      Company Registration Number: 20483957<br>
      Website: www.norvackdigital.example<br>
      email: info@norvackdigital.example<br>
      Phone: 01632 960 417<br>
      Address: 48 Elmstead Lane Loughborough<br>
      Leicestershire United Kingdom LE14 7QW
    </div>
    <svg class="swoosh" viewBox="0 0 100 100" preserveAspectRatio="none" aria-hidden="true">
      <path fill="var(--navy)" d="M0,72 C10,88 50,92 100,66 L100,69 C55,102 12,102 0,92 Z"/>
    </svg>
  </section>

  <section class="sheet card-back" aria-label="Business card back">
    <span class="brand brand--light">NORVACK DIGITAL</span>
  </section>

</main>
</body>
</html>
```